STATIONERY FOR OUR CLIENT

I have a client that is a major oilseed processor in Australia. They want a deluxe gorgeous version of their business card.
I am proposing we print the business cards in Pelbrix.com VARNO versions with the coloured edging, probably in black. Their business name needs to appear on both sides whether in logo or text.
The stationery needs to be layed up to look lifelike to impress the client. Ideally full stationery including letterhead, business card, with compliments, envelopes.
We want to impress our client.
*** The design needs to communicate - quality, premium, prestige, modern, expert, wealthy, abundant, sophisticated, established.
Designs need to be not too dark, not alot of black please. Clean, modern, sophisticated, upmarket, luxury brand.
I need 3 concepts to present to client and once approved, refined to then have print ready files - and working files just in case we have to make tweaks down the track.
We also need to create a one page style guide, that includes pms colour etc.
THIS IS AN URGENT JOB
Updates

Please design less with black more with clean white possibly light grey/beige as secondary colour if you are looking for contrast. I have added some examples of cards that look nice and might help with what the client is looking for. thank you and looking forward to seeing the designs

Please ensure all designs submitted have the correct contact details of our client which is in the brief. Also please do not have any black backgrounds - if any of your design do have black backgrounds, please amend. Thank you

Target Market(s)

business customers, investors, major distributors

Industry/Entity Type

Business

Font styles to use
Sans Serif

Requirements
Must have
• must have business name on both sides. designed to be printed with pelbrix.com using their VARNO business card print offering.
Should not have
• alot of black

```html
<!DOCTYPE html>
<html lang="en">
<head>
<meta charset="utf-8">
<title>KARO Business Card</title>
<link href="https://fonts.googleapis.com/css2?family=Roboto:wght@400;500&family=Roboto+Condensed:wght@400;500&display=swap" rel="stylesheet">
<style>
  :root {
    --backdrop: #e9e7e3;
    --card-light: #ffffff;
    --card-shade: #e4e5e4;
    --green-deep: #1f7a2e;
    --green-mid: #3f9a3d;
    --green-light: #7cc46f;
    --ink: #3a3a3a;
    --ink-soft: #666a66;
    --rule: #9a9c9a;
  }
  * { margin: 0; padding: 0; box-sizing: border-box; }
  html, body { width: 1200px; height: 970px; overflow: hidden; }
  body {
    background: var(--backdrop);
    font-family: "Roboto", sans-serif;
    color: var(--ink);
    position: relative;
  }
  .card {
    position: absolute;
    left: 250px;
    width: 700px;
    height: 400px;
    background: radial-gradient(ellipse at 40% 45%, var(--card-light) 0%, #f4f4f4 55%, var(--card-shade) 100%);
    box-shadow: 0 10px 28px rgba(0,0,0,0.18);
    overflow: hidden;
  }
  .card--front { top: 60px; }
  .card--back { top: 510px; }
  .card__bands { position: absolute; inset: 0; width: 700px; height: 400px; }

  .brand { position: absolute; }
  .brand__row { display: flex; align-items: center; gap: 16px; }
  .brand__dot {
    width: 46px; height: 46px; border-radius: 50%;
    background: var(--green-mid);
  }
  .brand__name {
    font-family: "Roboto", sans-serif;
    font-weight: 400;
    font-size: 40px;
    letter-spacing: 22px;
    color: var(--green-deep);
  }
  .brand__tagline {
    margin-top: 4px;
    margin-left: 62px;
    font-size: 17px;
    color: var(--green-mid);
  }
  .card--front .brand { left: 190px; top: 150px; }
  .card--back .brand { left: 48px; top: 160px; }
  .card--back .brand__name { font-size: 32px; letter-spacing: 17px; }
  .card--back .brand__dot { width: 38px; height: 38px; }
  .card--back .brand__tagline { font-size: 14px; margin-left: 54px; }

  .contacts {
    position: absolute;
    left: 330px; top: 95px;
    padding-left: 18px;
    border-left: 1.5px solid var(--rule);
    list-style: none;
  }
  .contacts::before {
    content: "";
    position: absolute;
    left: -1px; top: -6px;
    width: 170px;
    border-top: 1.5px solid var(--rule);
  }
  .contacts li {
    display: flex; align-items: center; gap: 9px;
    font-family: "Roboto Condensed", sans-serif;
    font-size: 13px;
    color: var(--ink-soft);
    height: 30px;
  }
  .contacts svg { width: 17px; height: 17px; flex: none; }

  .person {
    position: absolute;
    right: 34px; top: 205px;
    text-align: right;
    font-family: "Roboto Condensed", sans-serif;
  }
  .person__name { font-size: 27px; font-weight: 400; letter-spacing: 1px; color: var(--ink); }
  .person__role { font-size: 12px; letter-spacing: 2px; color: var(--ink-soft); margin-top: 2px; }
</style>
</head>
<body>

<section class="card card--front" aria-label="Business card front">
  <svg class="card__bands" viewBox="0 0 700 400" aria-hidden="true">
    <defs>
      <linearGradient id="frontGreen" x1="0" y1="0" x2="1" y2="1">
        <stop offset="0" stop-color="#8fd07f"/>
        <stop offset="1" stop-color="#1f7a2e"/>
      </linearGradient>
    </defs>
    <polygon points="560,0 610,0 700,62 700,96" fill="url(#frontGreen)"/>
    <polygon points="622,0 700,0 700,50" fill="#3f9a3d" opacity="0.85"/>
    <polygon points="0,292 40,318 40,400 0,400" fill="url(#frontGreen)"/>
    <polygon points="48,324 62,333 62,400 48,400" fill="#7cc46f"/>
  </svg>
  <div class="brand">
    <div class="brand__row">
      <span class="brand__dot"></span>
      <span class="brand__name">KARO</span>
    </div>
    <p class="brand__tagline">Kestrel Agri Oils &amp; Energy</p>
  </div>
</section>

<section class="card card--back" aria-label="Business card back">
  <svg class="card__bands" viewBox="0 0 700 400" aria-hidden="true">
    <defs>
      <linearGradient id="backGreen" x1="0" y1="0" x2="1" y2="0">
        <stop offset="0" stop-color="#1f7a2e"/>
        <stop offset="0.6" stop-color="#4fae45"/>
        <stop offset="1" stop-color="#9ad88a"/>
      </linearGradient>
    </defs>
    <polygon points="0,0 700,0 700,8 250,8 220,30 0,30" fill="url(#backGreen)"/>
    <polygon points="232,30 262,12 292,12 262,30" fill="#7cc46f"/>
    <rect x="656" y="16" width="36" height="36" fill="#5cb552"/>
    <polygon points="0,392 400,392 430,370 700,370 700,400 0,400" fill="url(#backGreen)"/>
    <polygon points="392,370 420,352 446,352 418,370" fill="#7cc46f"/>
  </svg>

  <div class="brand">
    <div class="brand__row">
      <span class="brand__dot"></span>
      <span class="brand__name">KARO</span>
    </div>
    <p class="brand__tagline">Kestrel Agri Oils &amp; Energy</p>
  </div>

  <ul class="contacts">
    <li>
      <svg viewBox="0 0 20 20" aria-hidden="true"><circle cx="10" cy="10" r="9" fill="none" stroke="#666a66" stroke-width="1.4"/><path d="M7 5.5l2 2-1 1.2c.6 1.3 1.6 2.3 2.9 2.9l1.2-1 2 2-1.3 1.4C9.6 13.6 6.4 10.4 5.6 7z" fill="#666a66"/></svg>
      014 552 7031
    </li>
    <li>
      <svg viewBox="0 0 20 20" aria-hidden="true"><circle cx="10" cy="10" r="9" fill="none" stroke="#666a66" stroke-width="1.4"/><rect x="7" y="5" width="6" height="10" rx="1" fill="none" stroke="#666a66" stroke-width="1.3"/></svg>
      014 552 7046
    </li>
    <li>
      <svg viewBox="0 0 20 20" aria-hidden="true"><circle cx="10" cy="10" r="9" fill="none" stroke="#666a66" stroke-width="1.4"/><rect x="6" y="8" width="8" height="6" fill="#666a66"/><rect x="7.5" y="5" width="5" height="3" fill="none" stroke="#666a66" stroke-width="1.2"/></svg>
      014 552 7058
    </li>
    <li>
      <svg viewBox="0 0 20 20" aria-hidden="true"><circle cx="10" cy="10" r="9" fill="none" stroke="#666a66" stroke-width="1.4"/><rect x="5.5" y="6.5" width="9" height="7" fill="none" stroke="#666a66" stroke-width="1.2"/><path d="M5.5 6.5l4.5 4 4.5-4" fill="none" stroke="#666a66" stroke-width="1.2"/></svg>
      alan@karoenergy.com
    </li>
    <li>
      <svg viewBox="0 0 20 20" aria-hidden="true"><circle cx="10" cy="10" r="9" fill="none" stroke="#666a66" stroke-width="1.4"/><circle cx="10" cy="10" r="5" fill="none" stroke="#666a66" stroke-width="1.2"/><path d="M5 10h10M10 5c-2 3-2 7 0 10M10 5c2 3 2 7 0 10" fill="none" stroke="#666a66" stroke-width="1"/></svg>
      www.karoenergy.com
    </li>
    <li>
      <svg viewBox="0 0 20 20" aria-hidden="true"><circle cx="10" cy="10" r="9" fill="none" stroke="#666a66" stroke-width="1.4"/><path d="M10 15s-3.5-3.6-3.5-6a3.5 3.5 0 0 1 7 0c0 2.4-3.5 6-3.5 6z" fill="#666a66"/><circle cx="10" cy="9" r="1.2" fill="#fff"/></svg>
      27 Mill Road, Wagga NSW
    </li>
  </ul>

  <div class="person">
    <p class="person__name">ALAN BRODY</p>
    <p class="person__role">GENERAL MANAGER</p>
  </div>
</section>

</body>
</html>
```